Web Design Concept for new social network

We need a fresh, vibrant, clean web design layout for a new social network that we are trying to put together.
The site itself will be stuffed with little jquery/css tricks to enable a better/better looking UI (this is where you come in).
Imagine you were re-imagining Chatterbox.. How would you have designed it? The new site, will have a lot of similar functions to CB, and then a few more.
I will need a great looking sign in page in addition to;
The main page will need to have the following elements;
- Profile header.
Profile picture and tabbed area for various pieces of meta data contact details, preferences etc
- A Post Wall (like the wall on CB, but its crossed with a quillet-esque global search/post). People can respond to not only the original message, but can reply to each individual reply.
Instead of LIKE, there will need to be a positive/negative/neutral style option (feel free to get creative with naming). The background of each post will reflect the average rating (pos/nuetral/neg) of the post itself.. so if 100 people click pos, 50 neutral and 1 negative, the bg will mainly be the positive colour).
The feed will include messages by default from many sources (chatterbox/quillet/worked up) there should be somewhere that these can be switched on and off...
Somewhere to post a message - again by default it will post to all networks, but should be able to switch off.
Images/Videos/Text can all be posted to the wall (if you can think of a better name than wall - please use that!)
- Notifications; rather than having them in a drop down menu like cb, i want them to be in a hidden div (one div for each type) that slides open to reveal the notifications.. The default will be that the divs are closed so if there is a new notification there will be a need for something to appear on the screen that the user can click. We will need 3 notification types.
- Calendar; collapsable
- Options for today/this week/month views etc
- Menu system to navigate to other screens.
This should be able to show available things like groups/pages/events (again feel free to rename).
The screens themselves should appear to be stacked (like stacked tiles).
- Search; there should be a search bar somewhere with various options being available.
- Modal popup. I will be using modal popups across the site so will want a consistant feel (should be able to display photos/videos etc)
I will upload some files over the next few days to support the above, but am really looking for your creativity here.
Sites I really like the style of:
- the NEW roomnest (check it out.. its awesome).
- plumb
- quillet
I want a really clean interface, modern.. splashes of colour are fine (but only where it will enhance).
Updates
I have added a file to the uploads that gives an idea of how the notifications should be revealed.. Please do not read too much into any styling... i created the pdf just to show how i expect the notifications to be revealed, and that I expect there to be multiple notification types.
Although I deliberately didnt request adverts to be shown in the brief, i also didnt explicitly state that they shouldnt be! The site will NOT feature adverts so please do not show them on the design. Id much rather that the space be used to improve layout.
Target Market(s)
18 to 40 - again, think chatterbox/quillet/workedup
Industry/Entity Type
Events
Look and feel

```html
<!DOCTYPE html>
<html lang="en">
<head>
<meta charset="utf-8">
<title>TheLoopHub.com – Profile</title>
<link href="https://fonts.googleapis.com/css2?family=Didact+Gothic&family=Questrial&family=Roboto:wght@400;700&display=swap" rel="stylesheet">
<style>
:root{
  --bg:#ecebea;
  --panel:#fbfafa;
  --panel-shade:#f3f2f1;
  --ink:#222;
  --muted:#555;
  --soft:#888;
  --red:#e6474d;
  --pink:#ff7c80;
  --dark:#3c3c3c;
  --line:#d9d9d9;
}
*{box-sizing:border-box;margin:0;padding:0}
html,body{width:1200px;height:1001px;overflow:hidden}
body{background:radial-gradient(circle at 70% 30%,#f4f3f2 0,#e9e8e7 70%);font-family:"Roboto",Arial,sans-serif;color:var(--ink);position:relative}
.abs{position:absolute}
.topline{left:0;top:0;width:1200px;height:3px;background:#555}
.usernav{left:677px;top:0;width:361px;height:32px;background:#5a5a5a;border-radius:0 0 4px 4px;display:flex;font-family:"Didact Gothic",sans-serif;font-size:14px;color:#eee}
.usernav span{flex:auto;text-align:center;line-height:30px;border-right:1px solid #777}
.usernav span:last-child{border:none}
.brand{font-family:"Questrial",sans-serif;font-size:22px;color:#555;font-weight:400}
.search{left:375px;top:40px;width:202px;height:32px;background:#fff;border:1px solid var(--line);font-family:"Didact Gothic",sans-serif;font-size:14px;color:#555;padding:7px 10px}
.search svg{position:absolute;right:10px;top:10px}
.sitenav{font-family:"Didact Gothic",sans-serif;font-size:16px;color:#555}
.btn-red{background:var(--red);color:#fff;border-radius:3px;text-align:center}
.sidebar{left:177px;top:106px;width:101px;height:235px;background:#444;border:2px solid #2e2e2e;border-radius:3px}
.photo{background:linear-gradient(160deg,#6c5a48,#b0775a 45%,#3a2c24)}
.sidebar .photo{position:absolute;left:8px;top:8px;width:82px;height:86px;border-radius:4px}
.sidebar .uname{position:absolute;left:11px;top:104px;font-family:"Questrial",sans-serif;font-weight:700;font-size:11px;color:#fff}
.sidebar ul{position:absolute;left:0;top:129px;width:97px;list-style:none}
.sidebar li{height:20px;font-family:"Questrial",sans-serif;font-size:10px;font-weight:700;color:#ddd;padding:4px 11px;border-top:1px solid #5a5a5a}
.sidebar li.on{background:#000;color:#fff;height:22px}
.friend{width:40px;height:40px;border:2px solid #fff;box-shadow:0 0 2px #aaa;background:linear-gradient(150deg,#d9b79b,#9a7457)}
.friends-count{left:177px;top:508px;width:101px;border-top:1px solid #ccc;padding-top:4px;font-size:10px;font-weight:700;color:#444}
.friends-count a{float:right;color:var(--red);font-weight:400;font-size:8px;text-decoration:underline}
.panel{background:var(--panel);border-radius:3px;box-shadow:0 1px 2px rgba(0,0,0,.08)}
.notes{left:285px;top:105px;width:752px;height:144px}
.note{position:absolute;left:18px;width:732px;height:17px;border-bottom:1px dotted #ccc;font-size:9px;color:var(--soft);padding-top:3px}
.note b{color:#222;font-weight:700}
.note i{font-style:normal;color:#222}
.note .ic{display:inline-block;width:12px;height:11px;border-radius:2px;vertical-align:-2px;margin-right:4px}
.tabicon{width:20px;height:21px;border-radius:2px}
.profile{left:285px;top:256px;width:752px;height:144px}
.pname{font-family:"Questrial",sans-serif;font-size:23px;font-weight:700;color:#555}
.meta{font-size:10px;color:#555}
.meta b{color:#222}
.facts{left:602px;top:277px;list-style:none;font-size:8.6px;color:#444;line-height:15px}
.facts li::before{content:"";display:inline-block;width:5px;height:5px;background:var(--red);margin:0 8px 1px -14px}
.sidetool{width:21px;height:21px;border-radius:3px;background:#d8d8d8;border:1px solid #c7c7c7}
.wall{left:285px;top:407px;width:750px;height:494px}
.composer{left:294px;top:416px;width:730px;height:91px;background:#ececec;border-radius:3px}
.field{background:#fff;border:1px solid #ccc;font-size:10px;color:#555;padding:11px 12px}
.small{font-size:10px;color:#555}
.red{color:var(--red)}
.post-text{font-size:9px;color:#444}
.likes{left:349px;top:649px;width:635px;height:22px;background:var(--pink);font-size:9px;color:#fff;padding:5px 0 0 23px}
.likes b{font-weight:400;color:#222}
.row{left:349px;width:635px;background:#e9e9e9;border-bottom:1px solid #d5d5d5;font-size:9px}
.avatar-s{width:28px;height:28px;border:1px solid #fff;background:linear-gradient(150deg,#e8c9a8,#b68a67)}
.footer{left:164px;top:922px;width:872px;border-top:1px solid #d5d5d5}
.links{left:166px;top:943px;font-size:10.5px;color:var(--red)}
.links span{color:#777;margin:0 2px}
</style>
</head>
<body>
<div class="abs topline"></div>
<nav class="abs usernav"><span>Updates</span><span>My Profile</span><span>Messages</span><span>Settings</span><span>Sign Out</span></nav>

<div class="abs brand" style="left:174px;top:42px">TheLoopHub.com</div>
<div class="abs search">Enter Keyword
  <svg width="11" height="11" viewBox="0 0 11 11"><circle cx="4.3" cy="4.3" r="3.3" fill="none" stroke="#555" stroke-width="1.6"/><line x1="6.8" y1="6.8" x2="10.2" y2="10.2" stroke="#555" stroke-width="2"/></svg>
</div>
<div class="abs sitenav btn-red" style="left:843px;top:44px;width:72px;height:28px;line-height:28px">Groups</div>
<div class="abs sitenav" style="left:931px;top:48px">Pages</div>
<div class="abs sitenav" style="left:990px;top:48px">Events</div>

<aside class="abs sidebar">
  <div class="photo" role="img" aria-label="Profile photo of Marcus Fenwick"></div>
  <div class="uname">Marcus Fenwick</div>
  <ul><li class="on">Wall</li><li>Photos</li><li>Videos</li><li>Pages</li><li>Groups</li></ul>
</aside>
<div class="abs friend" style="left:180px;top:349px" role="img" aria-label="Friend photo"></div>
<div class="abs friend" style="left:233px;top:349px" role="img" aria-label="Friend photo"></div>
<div class="abs friend" style="left:180px;top:402px" role="img" aria-label="Friend photo"></div>
<div class="abs friend" style="left:233px;top:402px" role="img" aria-label="Friend photo"></div>
<div class="abs friend" style="left:180px;top:455px" role="img" aria-label="Friend photo"></div>
<div class="abs friend" style="left:233px;top:455px" role="img" aria-label="Friend photo"></div>
<div class="abs friends-count">119 Friends <a>View All</a></div>

<section class="abs panel notes">
  <div class="note" style="top:22px"><span class="ic" style="background:#2a7fd4"></span><b>Delia Marsh</b> invited you to play Gem Rush. <i>9:44pm</i></div>
  <div class="note" style="top:40px"><span class="ic" style="background:#c9a66b"></span><b>Rafiq Dayal</b> changed the privacy of the group MaStI&amp; JoKe &amp;ShAiRi&amp; sMs&amp; lOvE&amp; oN CB from Open to Closed. <i>6:39pm</i></div>
  <div class="note" style="top:57px"><span class="ic" style="background:#8b96b8"></span><b>Anil Varma</b> changed the privacy of the group masti from Open to Secret. <i>10:44pm</i></div>
  <div class="note" style="top:75px"><span class="ic" style="background:#2a7fd4"></span><b>Delia Marsh</b> invited you to play Gem Rush. <i>6:15pm</i></div>
  <div class="note" style="top:92px"><span class="ic" style="background:#8b96b8"></span><b>Tariq Saleem</b> shared your photo. <i>12:34am</i></div>
  <div class="note" style="top:110px;border:none"><span class="ic" style="background:#c9a66b"></span><b>Anil Varma</b> changed the privacy of the group masti from Open to Secret. <i>10:44pm</i></div>
</section>
<div class="abs tabicon" style="left:943px;top:97px;background:#555"></div>
<div class="abs tabicon" style="left:971px;top:97px;background:#2b93d6"></div>
<div class="abs tabicon" style="left:998px;top:97px;background:var(--red);border-radius:50%"></div>

<section class="abs panel profile">
  <div class="abs photo" style="left:15px;top:17px;width:82px;height:85px;border-radius:6px;border:2px solid #222" role="img" aria-label="Profile photo of Marcus Fenwick"></div>
  <div class="abs btn-red" style="left:24px;top:111px;width:59px;height:18px;font-family:'Didact Gothic',sans-serif;font-size:14px;line-height:18px">Edit</div>
  <div class="abs pname" style="left:106px;top:16px">Marcus Fenwick</div>
  <div class="abs meta" style="left:106px;top:45px"><b>Birth :</b> April 22, 1980</div>
  <div class="abs meta" style="left:106px;top:60px"><b>Country :</b> UK</div>
  <div class="abs" style="left:287px;top:18px;width:2px;height:112px;background:linear-gradient(#fff,#d8d8d8,#fff)"></div>
</section>
<ul class="abs facts">
  <li>I'm Currently Live Portland, OR</li>
  <li>I'm in the Lakeside Ward</li>
  <li>I'm Single</li>
  <li>I Graduated from Ridgeview</li>
  <li>I served my Mission in Bogota. Colombia</li>
  <li>My Super power would be able to fly!</li>
  <li style="list-style:none" class="nobullet">I love business, Being Creative, Basketball, Coaching Basketball, Comedy and lots of Laughing...</li>
</ul>
<style>.facts li.nobullet::before{background:none}</style>
<div class="abs sidetool" style="left:1039px;top:272px;background:#f2f2f2"><svg width="19" height="19"><circle cx="9.5" cy="6" r="3.5" fill="#c8774a"/><path d="M3 17c0-5 13-5 13 0z" fill="var(--red)"/></svg></div>
<div class="abs sidetool" style="left:1039px;top:296px"><svg width="19" height="19"><circle cx="9.5" cy="9.5" r="5" fill="none" stroke="#888" stroke-width="2.5" stroke-dasharray="2 1.5"/><circle cx="9.5" cy="9.5" r="2" fill="#888"/></svg></div>
<div class="abs sidetool" style="left:1039px;top:320px"><svg width="19" height="19"><circle cx="9.5" cy="9.5" r="7" fill="#888"/><text x="8" y="13.5" font-size="10" font-style="italic" fill="#fff" font-family="serif">i</text></svg></div>

<section class="abs panel wall"></section>
<div class="abs composer"></div>
<div class="abs field" style="left:303px;top:425px;width:712px;height:34px">Dazzle the world... or just share something...</div>
<div class="abs small" style="left:303px;top:478px">Attach:</div>
<svg class="abs" style="left:348px;top:476px" width="65" height="16"><rect x="1" y="3" width="14" height="11" fill="#e9b65c" stroke="#2a7fd4"/><rect x="25" y="3" width="16" height="12" fill="#1e5f9e"/><rect x="50" y="3" width="12" height="11" fill="#fff" stroke="#777"/></svg>
<div class="abs small" style="left:437px;top:478px">Instant Invite:</div>
<svg class="abs" style="left:503px;top:471px" width="16" height="24"><rect x="5" y="1" width="4" height="12" rx="2" fill="#2b93d6"/><rect x="3" y="9" width="11" height="13" rx="4" fill="#2b93d6"/></svg>
<svg class="abs" style="left:928px;top:478px" width="22" height="10"><rect x="1" y="4" width="7" height="6" fill="#555"/><path d="M2.5 4V2.5a2 2 0 0 1 4 0V4" fill="none" stroke="#555"/><path d="M13 3h8l-4 4z" fill="#2b93d6"/></svg>
<div class="abs btn-red" style="left:955px;top:474px;width:60px;height:20px;font-family:'Didact Gothic',sans-serif;font-size:14px;line-height:20px">Share</div>

<div class="abs avatar-s" style="left:297px;top:524px;width:43px;height:44px;border-radius:4px;background:linear-gradient(150deg,#c89774,#6f4b34)" role="img" aria-label="Profile photo of post author"></div>
<div class="abs red" style="left:351px;top:525px;font-size:10.5px;font-weight:700">User Name Here</div>
<div class="abs" style="left:349px;top:543px;width:95px;height:75px;border:4px solid #fff;box-shadow:0 0 2px #aaa;background:linear-gradient(#9fc0d8,#6f8f5a 55%,#b33a3a 75%,#5b6a4a)" role="img" aria-label="Group photo outdoors"></div>
<div class="abs red" style="left:452px;top:544px;font-size:10px">Image Caption Here</div>
<div class="abs post-text" style="left:452px;top:558px;font-size:10px">yeah i got you back :PPPPPP</div>
<div class="abs red" style="left:452px;top:577px;font-size:8.5px">Like <span style="color:#bbb">&nbsp;|&nbsp;</span> Comment</div>
<div class="abs red" style="left:452px;top:604px;font-size:8.5px">Positive <span style="color:#bbb">&nbsp;|&nbsp;</span> Negative <span style="color:#bbb">&nbsp;|&nbsp;</span> Neutral</div>
<div class="abs small" style="left:349px;top:624px"><svg width="14" height="11" style="vertical-align:-1px"><rect x=".5" y="1" width="13" height="9" fill="#e9b65c" stroke="#2a7fd4"/></svg> 16 hours ago</div>
<svg class="abs" style="left:389px;top:641px" width="14" height="8"><path d="M0 8L7 0l7 8z" fill="var(--pink)"/></svg>
<div class="abs likes"><svg width="12" height="11" style="position:absolute;left:5px;top:5px"><path d="M1 5h3v6H1zM5 5l3-5c2 0 2 2 1 4h3v3l-2 4H5z" fill="#f3c05a"/></svg>Lena Brooks <b>and</b> Ana-Lucia Brooks <b>like this</b></div>
<div class="abs row" style="top:676px;height:21px;padding:5px 0 0 22px;font-style:italic;color:var(--red)"><svg width="13" height="11" style="position:absolute;left:5px;top:5px"><rect x=".5" y=".5" width="12" height="8" fill="none" stroke="#888"/></svg>Show all 12 comments</div>
<div class="abs row" style="top:702px;height:35px">
  <div class="abs avatar-s" style="left:4px;top:4px" role="img" aria-label="Commenter photo"></div>
  <div class="abs" style="left:41px;top:5px"><span class="red">Ana-Lucia Brooks</span> like this</div>
  <div class="abs" style="left:41px;top:20px;color:#555"><svg width="14" height="10" style="vertical-align:-1px"><rect x=".5" y=".5" width="13" height="9" fill="#e9b65c" stroke="#2a7fd4"/></svg> about an hour ago</div>
</div>
<div class="abs row" style="top:741px;height:36px">
  <div class="abs avatar-s" style="left:4px;top:4px" role="img" aria-label="Commenter photo"></div>
  <div class="abs" style="left:41px;top:6px"><span class="red">Ana-Lucia Brooks</span> like this</div>
  <div class="abs" style="left:41px;top:21px;color:#555"><svg width="14" height="10" style="vertical-align:-1px"><rect x=".5" y=".5" width="13" height="9" fill="#e9b65c" stroke="#2a7fd4"/></svg> about an hour ago</div>
</div>
<div class="abs field" style="left:349px;top:780px;width:635px;height:34px;font-family:'Didact Gothic',sans-serif;font-size:14px;padding:7px 10px">Drop some of your wisdom on em</div>
<div class="abs" style="left:348px;top:817px;width:635px;height:67px;border:1px solid #ccc;border-radius:3px;background:linear-gradient(#fbfbfb,#e9e9e9)">
  <svg class="abs" style="left:302px;top:19px" width="28" height="28" viewBox="-14 -14 28 28">
    <g fill="#333"><circle cx="0" cy="-10" r="2.4"/><circle cx="7" cy="-7" r="2.2" opacity=".9"/><circle cx="10" cy="0" r="2" opacity=".8"/><circle cx="7" cy="7" r="1.9" opacity=".7"/><circle cx="0" cy="10" r="1.8" opacity=".6"/><circle cx="-7" cy="7" r="1.7" opacity=".5"/><circle cx="-10" cy="0" r="1.6" opacity=".4"/><circle cx="-7" cy="-7" r="1.5" opacity=".3"/></g>
  </svg>
</div>

<div class="abs footer"></div>
<div class="abs links">About<span>-</span>Help<span>-</span>Blog<span>-</span>Status<span>-</span>Jobs<span>-</span>Terms<span>-</span>Privacy<span>-</span>Advertisers<span>-</span>Businesses<span>-</span>Media<span>-</span>Developers<span>-</span>Resources<span>-</span>Directory</div>
<div class="abs brand" style="left:857px;top:937px">TheLoopHub.com</div>
</body>
</html>
```